New Meal Prep Flyer for New Package Deals

We are looking for a design that displays our new packages that we offer. If you take a look at our website www.brambleforkmeals.com, and click on packages , you'll see the way we display them currently . We would like something similar to that in style . The first package is called "Horizon" and this package will be a 1 week package (7 days ), 2 meals a day, for a price of $195.00. The second package is called "Amber" and this package will be a 3 week package (21 days) 2 meals per day, for a price of $546.00 , the third package is a 6 week+ package (45 days), and it is called "Evergreen" , 2 meals per day , and the price is $1080.00 .
For the Amber Package , can you put next to it "Save $42.00!"
For the Evergreen Package, can you put next to it "Save $180!"
We also want our logo on the flyer (see attached), and we are just looking for a 1 page flyer , 8 1/2 x 11.

```html
<!DOCTYPE html>
<html lang="en">
<head>
<meta charset="utf-8">
<title>Bramblefork Meal Prep – Package Deals</title>
<link rel="stylesheet" href="https://fonts.googleapis.com/css2?family=DM+Sans:wght@500;600;700&family=Montserrat:wght@800;900&family=Oswald:wght@500;600&display=swap">
<style>
  :root{
    --green:#95c33f;
    --gray:#8a8a8a;
    --gray-dark:#7d7d7d;
    --light:#ededed;
    --navy:#27215f;
    --navy-glow:#3b3688;
    --white:#ffffff;
    --ink:#1b1b1b;
  }
  *{margin:0;padding:0;box-sizing:border-box}
  html,body{width:900px;height:1200px;overflow:hidden;background:var(--light)}
  .flyer{position:relative;width:900px;height:1200px;overflow:hidden;background:var(--light);font-family:"DM Sans",sans-serif}

  .brand{position:absolute;top:52px;left:0;width:900px;text-align:center}
  .brand-name{font-family:"DM Sans",sans-serif;font-weight:700;font-size:54px;letter-spacing:2px;color:var(--gray);line-height:1}
  .brand-tagline{margin-top:8px;font-family:"DM Sans",sans-serif;font-weight:700;font-size:19px;color:var(--green);letter-spacing:.2px}

  .headline-band{position:absolute;top:177px;left:0;width:900px;height:140px;background:var(--green);display:flex;align-items:center;justify-content:center}
  .headline{font-family:"DM Sans",sans-serif;font-weight:600;font-size:41px;line-height:1.2;color:var(--white);text-align:center;letter-spacing:.3px}

  .offer-stage{position:absolute;top:317px;left:0;width:900px;height:733px;background:radial-gradient(ellipse 60% 45% at 50% 75%,var(--navy-glow),var(--navy))}
  .card-shapes{position:absolute;top:0;left:0}

  .web-address{position:absolute;top:376px;left:280px;font-family:"Montserrat",sans-serif;font-weight:800;font-size:23px;letter-spacing:7.4px;color:var(--white)}

  .side-tab{position:absolute;font-family:"Montserrat",sans-serif;font-weight:800;color:var(--white);font-size:20px;letter-spacing:.5px;transform:rotate(-90deg);transform-origin:center;white-space:nowrap;text-align:center}
  .side-tab--horizon{left:50px;top:548px;width:120px}
  .side-tab--amber{left:730px;top:518px;width:120px}
  .tier-tab{position:absolute;left:174px;top:711px;width:250px;text-align:center;font-family:"Montserrat",sans-serif;font-weight:800;font-size:21px;color:var(--white);letter-spacing:.5px}

  .package{position:absolute}
  .package-title{font-family:"Montserrat",sans-serif;font-weight:900;font-size:33px;line-height:.9;color:var(--white);letter-spacing:.5px}
  .package-days{display:inline-block;margin-top:3px;padding:0 3px;font-family:"Montserrat",sans-serif;font-weight:800;font-size:20px;line-height:25px;color:var(--white)}
  .package-meals{width:172px;border-top:1.5px solid var(--white);border-bottom:1.5px solid var(--white);margin-top:10px;padding:6px 0 5px;font-family:"Montserrat",sans-serif;font-weight:800;font-size:17px;color:var(--white);letter-spacing:.6px;white-space:nowrap}
  .price-label{display:flex;align-items:flex-end;gap:1px;margin-top:6px;font-family:"Montserrat",sans-serif;font-weight:800;font-size:17px;color:var(--white);line-height:1}
  .price-label svg{width:26px;height:24px}
  .price{font-family:"Oswald",sans-serif;font-weight:600;font-size:62px;line-height:1;color:var(--white);letter-spacing:-.5px;margin-top:-2px}
  .price .currency{font-size:30px;margin-right:2px}

  .package--horizon{left:178px;top:447px}
  .package--horizon .package-days{background:var(--gray)}

  .package--amber{left:479px;top:447px}
  .package--amber .package-days{background:var(--green)}
  .package--amber .package-meals{width:171px}

  .package--evergreen{left:178px;top:773px}
  .package--evergreen .package-title{color:var(--green)}
  .package--evergreen .package-days{background:var(--gray)}
  .evergreen-pricing{position:absolute;left:470px;top:745px}
  .evergreen-pricing .package-meals{margin-top:0;width:172px;color:var(--gray);border-color:var(--gray)}
  .evergreen-pricing .price-label{color:var(--green)}
  .evergreen-pricing .price{color:var(--gray)}

  .save-badge{position:absolute;width:90px;height:90px;display:flex;flex-direction:column;align-items:center;justify-content:center;font-family:"Montserrat",sans-serif;font-weight:800;color:var(--white);line-height:1}
  .save-badge svg{position:absolute;inset:0}
  .save-badge span{position:relative}
  .save-badge .save-word{font-size:15px}
  .save-badge .save-amount{font-size:25px;margin-top:2px}
  .save-badge .save-amount small{font-size:15px}
  .save-badge--amber{left:659px;top:442px}
  .save-badge--evergreen{left:357px;top:760px}

  .app-row{position:absolute;top:1079px;left:0;width:900px;height:46px}
  .app-cta{position:absolute;left:151px;top:10px;font-family:"DM Sans",sans-serif;font-weight:600;font-size:19.5px;color:var(--ink)}
  .store-badge{position:absolute;top:0;height:46px;background:var(--ink);border-radius:5px}
  .store-badge--ios{left:455px;width:130px}
  .store-badge--android{left:596px;width:154px}
  .app-note{position:absolute;top:1132px;left:0;width:900px;text-align:center;font-family:"DM Sans",sans-serif;font-weight:500;font-size:12.6px;color:var(--ink)}
  .footer-strip{position:absolute;left:0;bottom:0;width:900px;height:18px}
</style>
</head>
<body>
<main class="flyer">

  <header class="brand">
    <div class="brand-name">BRAMBLEFORK</div>
    <div class="brand-tagline">HEALTHY KITCHEN&nbsp; | &nbsp;MEAL PREP</div>
  </header>

  <section class="headline-band">
    <h1 class="headline">Lip-smacking food<br>at pocket-friendly price!</h1>
  </section>

  <section class="offer-stage"></section>

  <svg class="card-shapes" width="900" height="1200" viewBox="0 0 900 1200" aria-hidden="true">
    <!-- gray upper band with top curve -->
    <path d="M230 415 H760 Q795 410 807 381 V705 H230 Z" fill="var(--gray)"/>
    <!-- lower light panel with speech tail -->
    <path d="M92 700 H807 V863 Q807 898 772 898 H230 Q190 898 165 930 L112 998 Q100 1012 92 1000 Z" fill="var(--light)"/>
    <!-- green first-package panel -->
    <path d="M128 381 H235 Q255 381 272 395 Q296 415 320 415 H429 V674 Q429 700 402 700 H92 V417 Q92 381 128 381 Z" fill="var(--green)"/>
    <!-- left tier tab -->
    <path d="M92 436 H116 Q128 440 128 452 V665 L92 683 Z" fill="var(--gray-dark)"/>
    <!-- right tier tab -->
    <path d="M807 417 V663 L784 655 Q772 652 772 640 V442 Q772 433 780 430 Z" fill="var(--green)"/>
    <!-- bottom tier tab -->
    <path d="M174 705 H420 L414 730 Q411 740 400 740 H206 Q196 740 190 730 Z" fill="var(--gray-dark)"/>
  </svg>

  <div class="web-address">www.brambleforkmeals.com</div>
  <div class="side-tab side-tab--horizon">HORIZON</div>
  <div class="side-tab side-tab--amber">AMBER</div>
  <div class="tier-tab">EVERGREEN</div>

  <article class="package package--horizon">
    <h2 class="package-title">1 WEEK<br>PACKAGE</h2>
    <div class="package-days">(7 DAYS)</div>
    <div class="package-meals">2 MEALS A DAY</div>
    <div class="price-label">
      <svg viewBox="0 0 26 24"><path d="M3 23 Q2 6 24 2 Q22 18 6 20 Z" fill="var(--white)"/></svg>PRICE
    </div>
    <div class="price"><span class="currency">$</span>195.00</div>
  </article>

  <article class="package package--amber">
    <h2 class="package-title">3 WEEK<br>PACKAGE</h2>
    <div class="package-days">(21 DAYS)</div>
    <div class="package-meals">2 MEALS PER DAY</div>
    <div class="price-label">
      <svg viewBox="0 0 26 24"><path d="M3 23 Q2 6 24 2 Q22 18 6 20 Z" fill="var(--green)"/></svg>PRICE
    </div>
    <div class="price"><span class="currency">$</span>546.00</div>
  </article>

  <div class="save-badge save-badge--amber">
    <svg viewBox="0 0 90 90"><circle cx="45" cy="45" r="41" fill="var(--green)" stroke="var(--green)" stroke-width="6" stroke-dasharray="1.6 1.6"/><circle cx="45" cy="45" r="33" fill="none" stroke="var(--white)" stroke-width="1.2" opacity=".5"/></svg>
    <span class="save-word">SAVE</span>
    <span class="save-amount"><small>$</small>42</span>
  </div>

  <article class="package package--evergreen">
    <h2 class="package-title">6 WEEK<br>PACKAGE</h2>
    <div class="package-days">(45 DAYS)</div>
  </article>

  <div class="save-badge save-badge--evergreen">
    <svg viewBox="0 0 90 90"><circle cx="45" cy="45" r="41" fill="var(--green)" stroke="var(--green)" stroke-width="6" stroke-dasharray="1.6 1.6"/><circle cx="45" cy="45" r="33" fill="none" stroke="var(--white)" stroke-width="1.2" opacity=".5"/></svg>
    <span class="save-word">SAVE</span>
    <span class="save-amount"><small>$</small>180</span>
  </div>

  <div class="evergreen-pricing">
    <div class="package-meals">2 MEALS PER DAY</div>
    <div class="price-label">
      <svg viewBox="0 0 26 24"><path d="M3 23 Q2 6 24 2 Q22 18 6 20 Z" fill="var(--green)"/></svg>PRICE
    </div>
    <div class="price"><span class="currency">$</span>1080.00</div>
  </div>

  <section class="app-row">
    <p class="app-cta">Order Food easily on our APP</p>
    <div class="store-badge store-badge--ios" role="img" aria-label="App store download badge"></div>
    <div class="store-badge store-badge--android" role="img" aria-label="Play store download badge"></div>
  </section>
  <p class="app-note">You can also download our mobile app from the play store and app store to choose your favorite meal from your favorite kitchen.</p>

  <svg class="footer-strip" viewBox="0 0 900 18" preserveAspectRatio="none" aria-hidden="true">
    <rect width="900" height="18" fill="var(--gray)"/>
    <path d="M670 18 L700 0 H900 V18 Z" fill="var(--green)"/>
  </svg>

</main>
</body>
</html>
```